CBD Boutique Business Card Needed

We are in need of a business card to reflect the direction of our latest products. We are a fully organic company in which our store and products are very heavy in wood and "natural" components. We decided to bring color into one of our brands and immediately knew this is where we needed to go.

We are NOT a cash grab CBD company. We could have done this wrong, slapped a label on a shit product and left it like that. I am passionate about sharing my experience with other veterans and opening a store and making it a comfortable place for others to come and see if they can have the same experience.

Target Market(s)

We are a dual market company. We do have a beauty line that will cover the costs of the majority of our business. But we also heavily cater to veterans and first responders. I am a veteran and this is how I found out about CBD. So the marketing needs to bring in our higher end beauty clientele but also be able to not put off our customers that readily need this.

Contact Information for Business Card

What we are looking for is a light, professional, boutique design that is is neither quite feminine or masculine. Attached is a picture of a store in Portland that we asked our store designer to get her inspiration from. But all natural wood and black outlines are what is mostly in there.

Attached are the following files:

Logo: An AI file with how we have our logo. I do not understand AI and have no idea why the letters are individual. The font is Adam. OLU is the logo and Tonics of Vigor is our tagline.

KM Vantage (front and back) cards I did originally found at a trade show that I absolutely loved...while it is mostly there and I would still be happy with them but it is me pretending to be you. I understand I am not and there is probably a lot wrong that all of you would see instantly and this is why I am here.

Dropper Bottle: This is our final product mock up

Water Color: I am semi flexible here. This water color is slightly different on every level of our brand. The color itself can change...we are not stuck on THIS particular one. If you happen to make a new one that is similar in style and we use it...then I will happily commission you to change the rest on our next product run. I am pretty sure you can use this statement as evidence later . =) .

But seriously, we heavily believe in pay it forward and will work with anyone here that may have a vision bigger than ours. The winner of this contest will get preferential consideration on our marketing materials (need letterhead etc. next, as well as a brochure, and website) so three more projects coming down the pipeline.

Information to use for your mockup is contained on the card images I have included. I would prefer CBD for wellness CBD for life to be more prominent. No where else on the card do we have CBD mentioned.

Font styles to use
Sans Serif

Colors

Designer to choose colors to be used in the design.

Requirements
Must have
• Double Sided
• Front: OLU logo on front of card will be raised embossed. Background is watercolor. One has been provided. Others are up for consideration. If the rest of your design is incredible and I don't like your watercolor I will just ask to swap it.
• Back: Standard information. Not stuck on anything here. I LOVE clean minimal designs. The bleed on the card I provided is a luxury...
• Font for title and OLU is Adam. Everything else I prefer san serif or as clean as possible.
Nice to have
• I Need to incorporate Gently Restoring somewhere on the card. Bold but not intrusive.

```html
<!DOCTYPE html>
<html lang="en">
<head>
<meta charset="UTF-8">
<title>OLU Business Card</title>
<link href="https://fonts.googleapis.com/css2?family=Lato:ital,wght@0,300;0,400;1,400&display=swap" rel="stylesheet">
<style>
  :root {
    --page: #ffffff;
    --card: #ffffff;
    --card-edge: #d4d4d4;
    --frame: #6d6d6d;
    --ink: #1c1c1c;
    --ink-soft: #555555;
    --ink-muted: #8a8a8a;
    --wash-blue: rgba(110, 196, 226, 0.55);
    --wash-blue-light: rgba(160, 218, 238, 0.45);
    --wash-green: rgba(170, 208, 110, 0.5);
    --wash-teal: rgba(120, 205, 200, 0.4);
  }
  * { margin: 0; padding: 0; box-sizing: border-box; }
  html, body {
    width: 1200px;
    height: 1200px;
    overflow: hidden;
    background: var(--page);
    font-family: "Lato", Arial, sans-serif;
    color: var(--ink);
  }
  .canvas { position: relative; width: 1200px; height: 1200px; }

  .card {
    position: absolute;
    left: 246px;
    width: 708px;
    height: 465px;
    background: var(--card);
    border: 1.5px solid var(--card-edge);
    overflow: hidden;
  }
  .card--front { top: 66px; }
  .card--back { top: 666px; }

  .watercolor { position: absolute; filter: blur(6px); }
  .card--front .watercolor {
    left: 120px; top: -10px; width: 500px; height: 490px;
    background:
      radial-gradient(ellipse 38% 40% at 28% 42%, var(--wash-green), transparent 72%),
      radial-gradient(ellipse 45% 48% at 64% 40%, var(--wash-blue), transparent 72%),
      radial-gradient(ellipse 40% 35% at 55% 78%, var(--wash-blue-light), transparent 75%),
      radial-gradient(ellipse 30% 30% at 20% 72%, var(--wash-teal), transparent 75%);
  }
  .card--back .watercolor {
    left: 110px; top: 0; width: 470px; height: 470px;
    background:
      radial-gradient(ellipse 34% 30% at 40% 12%, var(--wash-green), transparent 72%),
      radial-gradient(ellipse 42% 46% at 58% 38%, var(--wash-blue-light), transparent 72%),
      radial-gradient(ellipse 40% 42% at 50% 78%, var(--wash-blue), transparent 74%),
      radial-gradient(ellipse 28% 26% at 30% 55%, var(--wash-teal), transparent 75%);
  }

  .frame {
    position: absolute;
    left: 28px; top: 22px; right: 17px; bottom: 20px;
    border: 1.5px solid var(--frame);
  }

  .brand {
    position: absolute;
    left: 0; right: 0; top: 124px;
    text-align: center;
  }
  .brand__name {
    font-weight: 300;
    font-size: 172px;
    line-height: 1;
    letter-spacing: 0;
    color: var(--ink);
  }
  .brand__tagline {
    margin-top: -6px;
    font-weight: 300;
    font-size: 30px;
    line-height: 1.2;
    letter-spacing: 3px;
    text-transform: uppercase;
    color: var(--ink);
  }
  .motto {
    position: absolute;
    left: 0; right: 0; top: 405px;
    text-align: center;
    font-weight: 300;
    font-size: 20px;
    letter-spacing: 17px;
    color: var(--ink-muted);
  }

  .person {
    position: absolute;
    left: 0; right: 0; top: 70px;
    text-align: center;
  }
  .person__name { font-weight: 400; font-size: 40px; color: var(--ink); }
  .person__role {
    margin-top: 6px;
    font-style: italic;
    font-size: 22px;
    letter-spacing: 1px;
    color: var(--ink-soft);
  }

  .contact { position: absolute; left: 226px; top: 215px; list-style: none; }
  .contact__item {
    display: flex;
    align-items: center;
    margin-bottom: 18px;
    font-size: 18px;
    line-height: 1.25;
    color: var(--ink-soft);
  }
  .contact__icon { width: 44px; flex: none; display: flex; justify-content: center; margin-right: 12px; }
  .contact__icon svg { fill: var(--ink); }
</style>
</head>
<body>
<main class="canvas">

  <section class="card card--front" aria-label="Card front">
    <div class="watercolor" role="img" aria-label="Soft blue and green watercolor wash"></div>
    <div class="frame"></div>
    <div class="brand">
      <div class="brand__name">OLU</div>
      <div class="brand__tagline">Tonics of Vigor</div>
    </div>
    <p class="motto">Gently Restoring</p>
  </section>

  <section class="card card--back" aria-label="Card back">
    <div class="watercolor" role="img" aria-label="Soft blue and green watercolor wash"></div>
    <div class="person">
      <h1 class="person__name">Dana Whitfield</h1>
      <p class="person__role">OWNER / CEO</p>
    </div>
    <ul class="contact">
      <li class="contact__item">
        <span class="contact__icon">
          <svg width="26" height="36" viewBox="0 0 24 34" aria-hidden="true">
            <path d="M12 0C5.4 0 0 5.3 0 11.9 0 20.8 12 34 12 34s12-13.2 12-22.1C24 5.3 18.6 0 12 0zm0 16.5a4.6 4.6 0 1 1 0-9.2 4.6 4.6 0 0 1 0 9.2z"/>
          </svg>
        </span>
        <span>4120 N Cedar Ln<br>Mesa, AZ 85201<br>Suite 200</span>
      </li>
      <li class="contact__item">
        <span class="contact__icon">
          <svg width="30" height="30" viewBox="0 0 24 24" aria-hidden="true">
            <path d="M6.6 10.8c1.4 2.8 3.8 5.1 6.6 6.6l2.2-2.2c.3-.3.7-.4 1-.2 1.1.4 2.3.6 3.6.6.6 0 1 .4 1 1V20c0 .6-.4 1-1 1C10.6 21 3 13.4 3 4c0-.6.4-1 1-1h3.5c.6 0 1 .4 1 1 0 1.3.2 2.5.6 3.6.1.3 0 .7-.2 1L6.6 10.8z"/>
          </svg>
        </span>
        <span>480.555.0142</span>
      </li>
      <li class="contact__item">
        <span class="contact__icon">
          <svg width="38" height="26" viewBox="0 0 38 26" aria-hidden="true">
            <rect x="0" y="0" width="38" height="26" rx="2"/>
            <path d="M3 3l16 12L35 3" fill="none" stroke="#ffffff" stroke-width="2.5"/>
          </svg>
        </span>
        <span>olu@olu.life<br>www.olu.life</span>
      </li>
    </ul>
  </section>

</main>
</body>
</html>
```